Visitenkarte für therapeutischen Dienstleister
Breits die ersten Designvorschläge deckten sich weitgehend mit meinem Briefing. Anfragen und Änderungen werden rasch und professionell beantwortet und umgesetzt.
Zielgruppe
siehe Briefing
Aufgabenstellung

```html
<!DOCTYPE html>
<html lang="fr">
<head>
<meta charset="utf-8">
<title>Rivo-soin – cartes de visite</title>
<link href="https://fonts.googleapis.com/css2?family=Michroma&family=Arimo:wght@400;500&display=swap" rel="stylesheet">
<style>
  :root {
    --bg: #e9edef;
    --card: #ffffff;
    --ink: #111111;
    --accent: #d81e2a;
    --figure: #9a5a10;
    --figure-soft: #b5741f;
  }
  * { box-sizing: border-box; margin: 0; padding: 0; }
  html, body { width: 1200px; height: 900px; overflow: hidden; }
  body {
    background: var(--bg);
    display: flex;
    align-items: center;
    justify-content: center;
    gap: 40px;
    font-family: "Arimo", Arial, sans-serif;
    color: var(--ink);
  }
  .card {
    position: relative;
    width: 560px;
    height: 362px;
    background: var(--card);
    box-shadow: 0 2px 6px rgba(0,0,0,.12), 0 14px 30px rgba(0,0,0,.08);
    overflow: hidden;
  }
  .figure-art {
    position: absolute;
    top: 26px;
    right: 30px;
    width: 150px;
    height: 118px;
    border-radius: 40% 40% 30% 30%;
    background: radial-gradient(ellipse at 50% 45%, var(--figure-soft), var(--figure) 70%, rgba(154,90,16,0) 72%);
  }
  /* front */
  .brand {
    position: absolute;
    left: 70px;
    top: 150px;
    display: flex;
    align-items: center;
    gap: 14px;
  }
  .brand-dot {
    width: 22px; height: 22px;
    border-radius: 50%;
    background: var(--accent);
  }
  .brand-name {
    font-family: "Michroma", sans-serif;
    font-size: 44px;
    letter-spacing: 1px;
    color: var(--ink);
  }
  .tagline {
    position: absolute;
    left: 106px;
    top: 218px;
    font-family: "Michroma", sans-serif;
    font-size: 14px;
    letter-spacing: .5px;
  }
  /* back */
  .contact {
    position: absolute;
    left: 150px;
    top: 150px;
  }
  .person-name { font-size: 30px; font-weight: 500; }
  .person-role { font-size: 13px; margin-top: 4px; }
  .contact-list { list-style: none; margin-top: 16px; font-size: 13.5px; line-height: 1.4; }
  .contact-list li { display: flex; align-items: flex-start; gap: 10px; margin-bottom: 4px; }
  .contact-icon { flex: none; width: 16px; height: 16px; margin-top: 1px; }
</style>
</head>
<body>

<section class="card card-front">
  <div class="figure-art" role="img" aria-label="Illustration d'un corps humain bras écartés, en brun"></div>
  <div class="brand">
    <span class="brand-dot"></span>
    <span class="brand-name">Rivo-soin</span>
  </div>
  <p class="tagline">Thérapie musculo-squelettique</p>
</section>

<section class="card card-back">
  <div class="figure-art" role="img" aria-label="Illustration d'un corps humain bras écartés, en brun"></div>
  <div class="contact">
    <h1 class="person-name">Lionel Marchand</h1>
    <p class="person-role">masseur médical avec brevet fédéral</p>
    <ul class="contact-list">
      <li>
        <svg class="contact-icon" viewBox="0 0 16 16"><rect width="16" height="16" rx="3" fill="var(--accent)"/><path d="M8 3.5a3 3 0 0 0-3 3c0 2.2 3 5.5 3 5.5s3-3.3 3-5.5a3 3 0 0 0-3-3z" fill="#fff"/><circle cx="8" cy="6.5" r="1.1" fill="var(--accent)"/></svg>
        <span>Rue du Vallon 8,<br>1204 Genève</span>
      </li>
      <li>
        <svg class="contact-icon" viewBox="0 0 16 16"><rect width="16" height="16" rx="3" fill="var(--accent)"/><path d="M5 3.5l2 2-1 1.2c.6 1.3 1.6 2.3 2.8 2.8L10 8.5l2 2-1.2 1.5C7.5 11.8 4.2 8.5 3.5 5.2z" fill="#fff"/></svg>
        <span>079 000 12 34</span>
      </li>
      <li>
        <svg class="contact-icon" viewBox="0 0 16 16"><rect width="16" height="16" rx="3" fill="var(--accent)"/><rect x="3.5" y="5" width="9" height="6.5" fill="#fff"/><path d="M3.5 5l4.5 3.5L12.5 5" fill="none" stroke="var(--accent)" stroke-width="1"/></svg>
        <span>contact@rivo-soin</span>
      </li>
      <li>
        <svg class="contact-icon" viewBox="0 0 16 16"><rect width="16" height="16" rx="3" fill="var(--accent)"/><path d="M5 4l7 3.5-3 1 2.5 3-1.2 1-2.5-3L5.8 11z" fill="#fff"/></svg>
        <span>www.rivo-soin.ch</span>
      </li>
    </ul>
  </div>
</section>

</body>
</html>
```